Pilates Studio webdesign - Homepage design

Need a web design for this new Pilates studio.

1) Need elegant design that has great use of stock photos. See attached plumeframe lightbox. Use these for your designs
http://www.frameplume.com/search/lightbox/58120947

Be creative in how you use images. Could be a collage, or single image if design is strong.

2) Also see attached site map (PDF)

3) Please refer to this website for the "rollover section" on homepage. https://www.bookingacademy-varn.com/
We want similar functionality for "I'm Here Because"

4) See attached logos ZIP file.

5) My client kind of likes this website too:
http://motionhallq.com

Target Market(s)

mostly women

Number of Pages Required

2 page

Font styles to use
Sans Serif

Requirements
Must have
• strong design
• good use of stock image(s)
• logo included
Nice to have
• elegant design
Should not have
• not planning to build a long scrolling page.

```html
<!DOCTYPE html>
<html lang="en">
<head>
<meta charset="utf-8">
<title>Linden Studio — Pilates Homepage</title>
<link rel="stylesheet" href="https://fonts.googleapis.com/css2?family=Open+Sans:wght@400;600;700;800&display=swap">
<style>
:root{
  --orange:#f7931e;
  --orange-deep:#d9801a;
  --slate:#4f6b8d;
  --slate-dark:#34495e;
  --stone:#e5e3de;
  --paper:#f5f5f5;
  --white:#ffffff;
  --ink:#3a3a3a;
  --footer:#262626;
}
*{margin:0;padding:0;box-sizing:border-box}
html,body{width:1200px;height:2554px;overflow:hidden;background:var(--white);font-family:"Open Sans",Arial,sans-serif;color:var(--ink)}
.page{position:relative;width:1200px;height:2554px}
.column{position:absolute;left:144px;width:916px}

/* Hero */
.hero{top:0;height:475px;color:var(--white);overflow:hidden}
.hero-photo{position:absolute;inset:0;
  background:
    radial-gradient(ellipse 40% 50% at 18% 22%,rgba(235,225,205,.75),transparent 70%),
    radial-gradient(ellipse 30% 35% at 78% 35%,rgba(196,150,120,.6),transparent 70%),
    radial-gradient(ellipse 18% 16% at 86% 78%,rgba(150,40,50,.55),transparent 75%),
    radial-gradient(ellipse 22% 22% at 30% 82%,rgba(30,28,28,.8),transparent 75%),
    linear-gradient(180deg,#7a736b 0%,#5d5751 55%,#3b3633 100%)}
.hero-shade{position:absolute;inset:0;background:linear-gradient(180deg,rgba(0,0,0,.2),rgba(0,0,0,.15) 60%,rgba(0,0,0,.35))}
.brand{position:absolute;left:30px;top:14px;display:flex;align-items:center;gap:10px}
.brand-mark{width:38px;height:38px;border-radius:50%;background:var(--slate)}
.brand-name{font-size:15px;font-weight:700;color:var(--orange);letter-spacing:.5px;text-transform:uppercase;line-height:1.1}
.brand-tag{font-size:7px;color:var(--orange);letter-spacing:.5px;text-transform:uppercase}
.top-buttons{position:absolute;right:18px;top:12px;display:flex;gap:8px}
.pill{font-size:8px;font-weight:700;color:var(--white);padding:4px 12px;border-radius:10px;text-transform:uppercase}
.pill.slate{background:var(--slate)}
.pill.orange{background:var(--orange)}
.main-nav{position:absolute;right:20px;top:36px;display:flex;gap:22px;font-size:10px;font-weight:600}
.hero-copy{position:absolute;top:218px;width:100%;text-align:center}
.hero-welcome{font-size:30px;font-weight:400;letter-spacing:1px}
.hero-title{font-size:45px;font-weight:800;letter-spacing:1px}
.hero-sub{font-size:17px;margin-top:6px}
.btn{display:inline-block;background:var(--orange);color:var(--white);font-weight:700;text-transform:uppercase;border-radius:16px}
.hero .btn{margin-top:16px;font-size:14px;letter-spacing:3px;padding:7px 34px}

/* Reasons */
.reasons{top:475px;height:565px;background:var(--stone)}
.section-icon{position:absolute;left:50%;transform:translateX(-50%);width:28px;height:28px;border-radius:50%;border:5px solid var(--white)}
.reasons .section-icon{top:20px}
.reasons-title{position:absolute;top:58px;width:100%;text-align:center;font-size:22px;font-weight:700;color:var(--orange)}
.reasons-rule{position:absolute;top:72px;height:1px;background:#bdb9b2;width:190px}
.reasons-sub{position:absolute;top:98px;width:100%;text-align:center;font-size:10px}
.reason{position:absolute;top:150px;width:116px;height:116px;border-radius:50%;background:var(--slate);border:4px solid #cfd6df;color:var(--white);font-size:12px;font-weight:700;text-transform:uppercase;display:flex;align-items:center;justify-content:center;text-align:center;line-height:1.35}
.reason.active{background:var(--slate-dark);border-color:var(--slate-dark)}
.reason-panel{position:absolute;top:291px;left:134px;width:401px;height:196px;background:var(--white);padding:22px 20px}
.reason-panel h3{font-size:13px;font-weight:700;color:var(--slate-dark);text-transform:uppercase}
.reason-panel hr{width:50px;border:0;border-top:2px solid var(--orange);margin:8px 0 12px}
.reason-panel p{font-size:8.5px;line-height:1.5}
.join{position:absolute;top:291px;left:535px;width:259px;height:196px;color:var(--white);text-align:center;
  background:radial-gradient(ellipse 60% 50% at 60% 70%,rgba(120,140,165,.6),transparent 75%),linear-gradient(160deg,#5b7595,#445d7c)}
.join .section-icon{top:26px;border-color:rgba(255,255,255,.7)}
.join-title{position:absolute;top:68px;width:100%;font-size:21px;line-height:1.05;text-transform:uppercase}
.join .btn{position:absolute;top:128px;left:70px;font-size:9px;padding:4px 12px;border-radius:4px}

/* About */
.about{top:1040px;height:346px;color:var(--white);text-align:center;
  background:
    radial-gradient(ellipse 30% 30% at 30% 78%,rgba(120,60,10,.35),transparent 75%),
    radial-gradient(ellipse 30% 25% at 75% 82%,rgba(120,60,10,.3),transparent 75%),
    linear-gradient(180deg,var(--orange) 0%,var(--orange) 50%,var(--orange-deep) 100%)}
.about .section-icon{top:30px}
.about-eyebrow{position:absolute;top:66px;width:100%;font-size:9px;font-weight:700}
.about-title{position:absolute;top:80px;width:100%;font-size:24px;font-weight:700;text-transform:uppercase}
.about-text{position:absolute;top:118px;left:220px;width:470px;font-size:9px;line-height:1.55}
.about-photo{position:absolute;z-index:2;left:471px;top:1236px;width:228px;height:280px;background:var(--white);padding:8px;box-shadow:0 2px 8px rgba(0,0,0,.25)}
.about-photo div{width:100%;height:100%;
  background:
    radial-gradient(ellipse 30% 22% at 45% 38%,rgba(235,200,175,.9),transparent 70%),
    radial-gradient(ellipse 35% 45% at 50% 78%,rgba(35,40,48,.9),transparent 75%),
    linear-gradient(90deg,#2f3a48 0%,#c9d3dc 25%,#e6ebef 60%,#a9b4bf 100%)}

/* Practice */
.practice{top:1386px;height:679px;background:var(--paper)}
.photo-small{position:absolute;z-index:1;left:284px;top:1607px;width:270px;height:263px;background:var(--white);padding:5px}
.photo-large{position:absolute;z-index:1;left:442px;top:1687px;width:500px;height:330px;background:var(--white);padding:5px}
.photo-small div{width:100%;height:100%;
  background:
    radial-gradient(ellipse 22% 40% at 55% 40%,rgba(20,20,20,.95),transparent 75%),
    linear-gradient(90deg,#1e1e1e 0%,#1e1e1e 8%,#d8d8d8 20%,#f2f2f2 50%,#bdbdbd 80%,#2a2a2a 100%)}
.photo-large div{width:100%;height:100%;
  background:
    radial-gradient(ellipse 20% 35% at 58% 62%,rgba(15,15,15,.95),transparent 75%),
    radial-gradient(ellipse 50% 30% at 40% 92%,rgba(20,20,20,.85),transparent 75%),
    linear-gradient(90deg,#ececec 0%,#f7f7f7 30%,#d0d0d0 60%,#8a8a8a 85%,#1e1e1e 100%)}
.practice-title{position:absolute;z-index:2;left:577px;top:1622px;font-size:24px;font-weight:700;color:var(--slate-dark);text-transform:uppercase}
.practice-text{position:absolute;z-index:2;left:580px;top:1660px;width:362px;font-size:9px;line-height:1.4}

/* Scheduling */
.schedule{top:2065px;height:143px;background:var(--slate);color:var(--white);text-align:center}
.schedule .section-icon{top:14px}
.schedule-eyebrow{position:absolute;top:50px;width:100%;font-size:22px;letter-spacing:4px;text-transform:uppercase}
.schedule-title{position:absolute;top:82px;width:100%;font-size:34px;font-weight:700;text-transform:uppercase}

/* Referral */
.referral{top:2208px;height:302px;color:var(--white);
  background:
    radial-gradient(ellipse 18% 30% at 62% 30%,rgba(60,50,45,.55),transparent 75%),
    radial-gradient(ellipse 35% 14% at 70% 92%,rgba(90,60,110,.7),transparent 75%),
    radial-gradient(ellipse 12% 8% at 90% 85%,rgba(220,60,90,.6),transparent 75%),
    linear-gradient(90deg,#6b6c63 0%,#878679 45%,#a39d90 100%)}
.referral-mark{position:absolute;left:130px;top:38px;width:42px;height:42px;border-radius:50%;background:var(--slate)}
.referral-eyebrow{position:absolute;left:138px;top:86px;font-size:24px;text-transform:uppercase}
.referral-title{position:absolute;left:138px;top:114px;font-size:38px;font-weight:700;text-transform:uppercase}
.referral .btn{position:absolute;left:138px;top:176px;font-size:14px;padding:8px 22px;border-radius:6px}

/* Footer */
.footer{top:2510px;height:44px;background:var(--footer);color:#cfcfcf}
.socials{position:absolute;left:136px;top:13px;display:flex;gap:6px}
.socials span{width:16px;height:16px;border-radius:50%;background:var(--orange)}
.footer-links{position:absolute;right:18px;top:9px;font-size:8px;text-align:right;line-height:1.5}
</style>
</head>
<body>
<div class="page">

  <header class="column hero">
    <div class="hero-photo" role="img" aria-label="Woman training with an exercise ball and dumbbells in a bright gym"></div>
    <div class="hero-shade"></div>
    <div class="brand">
      <span class="brand-mark"></span>
      <div>
        <div class="brand-name">Linden Studio</div>
        <div class="brand-tag">Pilates studio for strength and grace</div>
      </div>
    </div>
    <div class="top-buttons">
      <span class="pill slate">Contact us</span>
      <span class="pill orange">Make an appointment</span>
    </div>
    <nav class="main-nav">
      <span>I'm Here Because</span><span>About Marlowe</span><span>What is Linden Studio</span><span>Scheduling sessions</span><span>Referrals</span>
    </nav>
    <div class="hero-copy">
      <div class="hero-welcome">WELCOME TO</div>
      <div class="hero-title">BUILD YOUR BODY STRONG</div>
      <div class="hero-sub">Lorem Ipsum is simply dummy text of the printing and typesetting industry.</div>
      <span class="btn">Read more</span>
    </div>
  </header>

  <section class="column reasons">
    <span class="section-icon"></span>
    <div class="reasons-rule" style="left:132px"></div>
    <div class="reasons-rule" style="right:58px"></div>
    <h2 class="reasons-title">I'M HERE BECAUSE</h2>
    <p class="reasons-sub">Lorem ipsum dolor sit amet, consectetur adipiscing elit. Duis ullamcorper eros nec sapien.</p>
    <div class="reason active" style="left:136px">Pilates</div>
    <div class="reason" style="left:274px">Back &amp;<br>Joint Pain</div>
    <div class="reason" style="left:403px">Stretching</div>
    <div class="reason" style="left:532px">Mobility &amp;<br>Stability</div>
    <div class="reason" style="left:669px">Strengthen<br>Body</div>
    <div class="reason-panel">
      <h3>Pilates</h3>
      <hr>
      <p>Lorem Ipsum is simply dummy text of the printing and typesetting industry. Lorem Ipsum has been the industry's standard dummy text ever since the 1500s, when an unknown printer took a galley of type and scrambled it to make a type specimen book. It has survived not only five centuries, but also the leap into electronic typesetting, remaining essentially unchanged. It was popularised in the 1960s with the release of Letraset sheets containing Lorem Ipsum passages, and more recently with desktop publishing software like Aldus PageMaker including versions of Lorem Ipsum.</p>
    </div>
    <div class="join" role="img" aria-label="Studio photo under a blue tint">
      <span class="section-icon"></span>
      <div class="join-title">Click here<br>to join us</div>
      <span class="btn">Make an appointment</span>
    </div>
  </section>

  <section class="column about" role="img" aria-label="Woman lying on a mat under an orange tint">
    <span class="section-icon"></span>
    <div class="about-eyebrow">ABOUT ME</div>
    <h2 class="about-title">About Marlowe</h2>
    <p class="about-text">Lorem Ipsum is simply dummy text of the printing and typesetting industry. Lorem Ipsum has been the industry's standard dummy text ever since the 1500s, when an unknown printer took a galley of type and scrambled it to make a type specimen book.</p>
  </section>

  <section class="column practice"></section>
  <div class="about-photo"><div role="img" aria-label="Instructor stretching one leg high on a Pilates reformer frame"></div></div>
  <div class="photo-small"><div role="img" aria-label="Black and white photo of a woman hanging from Pilates straps"></div></div>
  <div class="photo-large"><div role="img" aria-label="Black and white photo of a woman exercising on a Pilates cadillac frame"></div></div>
  <h2 class="practice-title">What is Linden Studio</h2>
  <p class="practice-text">Lorem Ipsum is simply dummy text of the printing and typesetting industry. Lorem Ipsum has been the industry's standard dummy text ever since the 1500s.</p>

  <section class="column schedule">
    <span class="section-icon"></span>
    <div class="schedule-eyebrow">Click here to know our</div>
    <h2 class="schedule-title">Scheduling sessions</h2>
  </section>

  <section class="column referral" role="img" aria-label="Woman in a deep lunge stretch on a mat against a concrete wall">
    <span class="referral-mark"></span>
    <div class="referral-eyebrow">Thanks so much for</div>
    <h2 class="referral-title">Your referral!</h2>
    <span class="btn">Make an appointment</span>
  </section>

  <footer class="column footer">
    <div class="socials"><span></span><span></span><span></span><span></span><span></span><span></span></div>
    <div class="footer-links">Site Map | Privacy and legal<br>© Copyright 2016. All rights reserved.</div>
  </footer>

</div>
</body>
</html>
```